Brightfield Training Course Outline re-design

We are wanting to re-design our template for course outlines. Course outlines are provided to prospective students wanting to find out more information about a course. Our website was recently revamped so we would want the new course outlines to have a similar look and feel to our website: www.brightfieldtraining.com.au
I have attached a current course outline. All content from the current outline must come across to the new one. We want to appeal to adult students wanting to work with children. We emphasise flexible timeframes, easy-to-use online system, prompt and friendly support from a trainer. We want to inspire people to engage in education and change their lives. This is reflected in our motto - Study | Brightfield | Achieve.
Ideally, this will become a template for other course outlines, so if the file can be provided in PDF as well as an editable format it would be greatly appreciated.
The colour codes from our website are:
Aqua: #81c9bd
Grey: #939598
Blue: #000080
Looking forward to responses.
Happy to email any images or logos needed.

Target Market(s)

Mums with children wanting to re-enter the workforce

Requirements
Must have
• All content from current course outline must come across.
• Brightfield Training logo

```html
<!DOCTYPE html>
<html lang="en">
<head>
<meta charset="utf-8">
<title>Brightfield Training – Course Outline CHC30213</title>
<link href="https://fonts.googleapis.com/css2?family=Open+Sans:wght@400;600;700&display=swap" rel="stylesheet">
<style>
:root{
  --aqua:#81c9bd;
  --grey:#939598;
  --navy:#000080;
  --bar:#22226e;
  --text:#3a3a3a;
  --bg:#e6e7e8;
  --white:#ffffff;
}
*{box-sizing:border-box;margin:0;padding:0}
html,body{width:886px;height:1200px;overflow:hidden;background:var(--bg)}
body{position:relative;font-family:"Open Sans",Arial,sans-serif;color:var(--text)}
.page{position:absolute;width:366px;height:518px;background:var(--white);overflow:hidden}
.p1{left:46px;top:54px}.p2{left:456px;top:54px}.p3{left:46px;top:618px}.p4{left:456px;top:618px}
.footer-bar{position:absolute;left:0;right:0;bottom:0;height:14px;background:var(--bar)}
.photo{position:absolute}
.txt{font-size:5.3px;line-height:1.32;text-align:justify}
.txt p{margin-bottom:3px}
.txt ul{list-style:none;margin-bottom:3px}
.txt li{padding-left:4px;text-indent:-4px}
.txt li::before{content:"• "}
.h{font-size:6.4px;color:var(--navy);font-weight:600;text-transform:uppercase;margin:4px 0 3px;display:flex;align-items:center;gap:3px}
.h::before{content:"";width:7px;height:7px;background:var(--navy);display:inline-block}
.h.plain::before{display:none}
.sub{color:var(--navy);font-weight:600;font-size:5.6px;margin:3px 0 2px}
.col{position:absolute}
/* page 1 */
.brand{position:absolute;left:24px;top:24px;font-size:19px;font-weight:700;color:var(--navy);letter-spacing:-.3px}
.modes{position:absolute;right:0;top:0;width:108px;height:90px;background:var(--aqua);clip-path:polygon(0 0,100% 0,100% 78%,0 100%);color:var(--white);font-size:8.4px;text-align:center;line-height:1.6;padding-top:14px}
.motto{position:absolute;left:0;top:258px;width:366px;height:20px;display:flex;gap:2px}
.motto span{flex:1;color:var(--white);font-size:11.5px;display:flex;align-items:center;justify-content:center;background:var(--aqua)}
.motto span.mid{background:var(--grey)}
.title{position:absolute;top:292px;left:0;width:366px;text-align:center;color:var(--navy);font-weight:700;font-size:9.6px}
/* page 3 */
.assess{position:absolute;left:183px;top:0;width:183px;height:138px;background:var(--aqua);color:var(--white);font-size:5.5px;line-height:1.3;padding:26px 10px 0 8px}
.assess p{margin-bottom:5px}
.fees{position:absolute;left:6px;top:382px;width:354px;border:1px solid var(--aqua);border-collapse:collapse;font-size:7px}
.fees th{background:var(--aqua);color:var(--white);font-weight:400;text-align:left;padding:4px 7px;font-size:9px}
.fees th+th,.fees td+td{text-align:center;width:96px;border-left:1px solid var(--aqua)}
.fees td{padding:6px 7px;border-top:1px solid var(--aqua);vertical-align:middle;line-height:1.4}
/* page 4 */
.enrol{position:absolute;left:0;top:382px;width:366px;height:116px;background:var(--aqua)}
.enrol .notch{position:absolute;left:176px;top:0;width:0;height:0;border-left:9px solid transparent;border-right:9px solid transparent;border-top:8px solid var(--white)}
.enrol .how{position:absolute;left:10px;top:16px;width:176px;font-size:5.4px;line-height:1.35;color:var(--navy)}
.enrol .how b{font-weight:600}
.enrol .brand2{position:absolute;left:205px;top:14px;font-size:15px;font-weight:700;color:var(--navy)}
.contacts{position:absolute;left:205px;top:50px;font-size:5.6px;color:var(--navy);line-height:1.75;list-style:none}
.contacts li{display:flex;align-items:center;gap:3px}
.contacts li::before{content:"";width:5px;height:5px;border-radius:50%;background:var(--white)}
</style>
</head>
<body>

<!-- Page 1 -->
<section class="page p1">
  <div class="brand">Brightfield Training</div>
  <div class="modes">CORRESPONDENCE<br>ONLINE<br>SELF PACED<br>BLENDED</div>
  <div class="photo" style="left:0;top:68px;width:366px;height:190px;background:linear-gradient(120deg,#c9a27a,#e9d8c4 45%,#b98d6a 75%,#7a9ab8)" role="img" aria-label="Teacher aide working with a group of young students at a classroom table"></div>
  <div class="motto"><span>STUDY</span><span class="mid">BRIGHTFIELD</span><span>ACHIEVE</span></div>
  <h1 class="title">COURSE OUTLINE: CHC30213 Certificate III in Education Support</h1>
  <div class="col txt" style="left:10px;top:312px;width:346px">
    <p>Welcome to Brightfield Training (RTO# 40817)! Thank you for considering us in the very important task of gaining a nationally recognised qualification. Please read this course outline and the student handbook prior to enrolling, these documents contain information crucial for successful study in this course.</p>
    <div class="sub">ABOUT CERTIFICATE III IN EDUCATION SUPPORT</div>
    <p>This course is suitable if you are currently working as or seeking to work as a teacher aide in a primary, secondary or special needs school or community education setting. This Nationally Recognised course consists of 17 units:</p>
    <ul style="text-align:left">
      <li>CHCECE006 Support behaviour of children and young people</li>
      <li>CHCEDS001 Comply with legislative, policy and industrial requirements in the education environment</li>
      <li>CHCEDS007 Work effectively with students and colleagues</li>
      <li>CHCEDS016 Support learning for students with disabilities in a classroom environment</li>
      <li>CHCEDS018 Support students with additional needs in the classroom environment</li>
      <li>CHCEDS002 Assist implementation of planned educational programs</li>
      <li>CHCEDS003 Contribute to student education in all developmental domains</li>
      <li>CHCDIV001 Work with diverse people</li>
      <li>CHCEDS008 Comply with school administrative requirements</li>
      <li>CHCEDS004 Contribute to organisation and management of classroom or centre</li>
      <li>CHCEDS005 Support the development of literacy and oral language skills</li>
      <li>CHCEDS006 Support the development of numeracy skills</li>
      <li>CHCEDS017 Contribute to the health and safety of students</li>
      <li>HLTWHS001 Participate in work health and safety</li>
      <li>CHCDIV002 Promote Aboriginal and/or Torres Strait Islander cultural safety</li>
    </ul>
  </div>
  <div class="footer-bar"></div>
</section>

<!-- Page 2 -->
<section class="page p2">
  <div class="photo" style="left:0;top:0;width:366px;height:131px;background:linear-gradient(110deg,#8fb3c9,#e7c9a8 40%,#d9a986 65%,#7fae7a)" role="img" aria-label="Smiling educator hugging a group of young children in a bright classroom"></div>
  <div style="position:absolute;left:0;top:134px;width:366px;height:4px;background:var(--aqua)"></div>
  <div class="col txt" style="left:10px;top:152px;width:172px">
    <div class="h plain">Elective units (Choose 2 from the following)</div>
    <ul style="text-align:left">
      <li>CHCEDS024 Use educational strategies to support Aboriginal and/or Torres Strait Islander education</li>
      <li>CHCEDS032 Support learning and implementation of responsible behaviour</li>
      <li>CHCEDS012 Set up and sustain individual and small group learning areas</li>
      <li>CHCEDS011 Search and assess online information</li>
      <li>CHCDIS004 Communicate using augmentative and alternative communication strategies</li>
    </ul>
    <p>HLTAID003 Provide first aid*<br>Please read the first aid section in this document for further details on fees and conditions associated with selecting this unit as an elective.</p>
    <div class="h">Entry requirements</div>
    <p>It is expected that students have well developed written and verbal communication skills, basic numeracy skills and basic computer operating skills. A working with children check (also known as a blue card in Qld) must be obtained prior to conducting your vocational placement. Refer back to our website for links to each State or Territory agency responsible for administering working with children checks.</p>
    <div class="h">Duration</div>
    <p>You will have up to 2 years to complete but can progress at any pace. As a guide someone spending 8 hrs per week on assessment, could expect to complete the course in approximately 7 - 9 months. Please note that students receiving government funding/subsidies may be obligated to complete in a set time frame:</p>
    <ul><li>StudyAssist Office (education supplement): full time 40 weeks, part time 69 weeks</li></ul>
  </div>
  <div class="col txt" style="left:190px;top:152px;width:166px">
    <div class="h">Study mode</div>
    <p>Delivery and assessment of this course can be customised. Please discuss your options with Brightfield to ensure that we have created the course that best suits you. Self-paced study means that you can study at times and locations that suit you. No assessment due dates and no timetabled lectures or webinars. You can choose to study online using an interactive student portal or via correspondence with all materials posted out to you. Fast track your study or take your time – the choice is yours. Blended study has all the perks of self-paced study with the addition of face-to-face sessions with your trainer. You can book as many or as few face-to-face sessions as you like – the price in the table below is based on four face-to-face sessions.</p>
    <div class="sub">ONLINE OR CORRESPONDENCE?</div>
    <p>The course consists of two key components – Theory and Practical. For the theory component you may opt to receive course resources by correspondence or online.</p>
    <ul>
      <li>Online: benefit from an easy to navigate elearning course. The online course is interactive, meaning less readings and more visually engaging resources.</li>
      <li>Correspondence: receive course resources such as textbooks and assessments in a hardcopy format. Resources are presented in a student portfolio for easy management. Assessment is provided on a USB stick.</li>
    </ul>
    <div class="h">Practical</div>
    <p>Students not currently working in the education support industry will be required to complete 100 hours practical placement as part of their study. You may choose to do your placement as a full time block or part time (e.g. 2 days per week). The placement can be completed at any stage during your course. Brightfield Training can arrange your placement for you or you can arrange your own. Additional hours (up to 100hrs) of placement may be required for school based students, students on a traineeship, Early School leavers or those that have been assessed as having limited work/life experience. This will enable more time to develop skills in a work setting. In some instances the exact number of practical placement hours will need to be negotiated between the student, the trainer and the placement person.</p>
  </div>
  <div class="footer-bar"></div>
</section>

<!-- Page 3 -->
<section class="page p3">
  <div class="photo" style="left:0;top:0;width:183px;height:138px;background:linear-gradient(120deg,#9cc7d8,#d8b79a 50%,#6b8fb3)" role="img" aria-label="Mother helping two children with drawing and homework at a table"></div>
  <div class="assess">
    <p style="text-transform:uppercase">Assessment</p>
    <p>Your assessment consists of two key areas:</p>
    <p>Theory assessment that may include:<br>text activities, written questions, case studies, projects, evidence portfolios.</p>
    <p>Practical assessment that includes:<br>demonstration of your skills in the workplace. Recorded as observations by your supervisor, practical placement person or trainer.</p>
  </div>
  <div class="col txt" style="left:8px;top:148px;width:172px">
    <div class="h">Government funding</div>
    <p>This course is approved for funding through the following agencies/programs:</p>
    <ul>
      <li>Certificate 3 Guarantee (eligible QLD residents only)</li>
      <li>Commonwealth Traineeships (for new employees)</li>
      <li>StudyAssist Office (Education Supplement)</li>
    </ul>
    <p>Contact us or complete our eligibility checklist and we will let you know if you or your employer may attract funding.</p>
    <div class="sub">Certificate 3 Guarantee</div>
    <p>The Certificate 3 Guarantee aims to assist people gain their first post school Certificate III qualification regardless of their current employment status. To be eligible for this program you must:</p>
    <ul>
      <li>Be aged 15 years or above and no longer be at school</li>
      <li>Permanently reside in Queensland</li>
      <li>Be an Australian citizen or New Zealand citizen or Australian permanent resident (including humanitarian entrants), or a temporary resident with the necessary visa and work permits on the pathway to permanent residency.</li>
    </ul>
  </div>
  <div class="col txt" style="left:190px;top:148px;width:168px">
    <ul><li>Not hold (or be currently enrolled in) a post school Certificate III or higher level qualification.</li></ul>
    <p>Students approved for the Certificate 3 Guarantee program will pay a student contribution fee. Concession card holders, Aboriginal or Torres Strait Islander people and students who have graduated year 12 within the last 12 months will receive a concession rate.</p>
    <div class="h">Payment</div>
    <p><b style="color:var(--navy)">Note:</b> fees quoted below are inclusive of all mandatory course resources. Additional fees apply if you choose the unit HLTAID003 Apply first aid as an elective unit. Please read the first aid section in this document for further details.</p>
    <p><b style="color:var(--navy)">Note:</b> Add $800 to above prices if you would like the blended mode of training (includes 4 onsite sessions and is only available to those in SE QLD region).</p>
    <p><b style="color:var(--navy)">Payment plans</b> are offered at no additional cost! All Fees quoted above can be incorporated into a payment plan. You nominate the payment periods (i.e. weekly, fortnightly or monthly). You nominate the instalment amount you are comfortable paying each period (i.e. $50, $100, $200, etc.).</p>
  </div>
  <table class="fees">
    <tr><th>CHC30213 Certificate III in Education Support</th><th>Self-Paced</th></tr>
    <tr><td>Standard course fee including those receiving the Education Supplement (through StudyAssist Office), OR;</td><td>$1,980</td></tr>
    <tr><td>For students who qualify for the Certificate 3 Guarantee:<br>• Standard Student contribution fee<br>• Student contribution fee - concessional students<br>• Student contribution fee - Yr 12 fee free students</td><td><br>$500<br>$400<br>$0</td></tr>
  </table>
  <div class="footer-bar"></div>
</section>

<!-- Page 4 -->
<section class="page p4">
  <div class="photo" style="left:0;top:0;width:366px;height:130px;background:linear-gradient(100deg,#3c4a55,#5d6b74 45%,#c9a58a 70%,#e8e2dc)" role="img" aria-label="Smiling young woman sitting in front of a classroom chalkboard"></div>
  <div style="position:absolute;left:0;top:134px;width:366px;height:4px;background:var(--aqua)"></div>
  <div class="col txt" style="left:10px;top:152px;width:172px">
    <div class="h">Student support</div>
    <p>Regardless of the study mode you select, you will have unlimited access to your trainer through phone, email and instant messaging. You may send your trainer drafts for feedback and comments. Each trainer has significant industry experience and will prove to be a valuable support network for you throughout the course.</p>
    <div class="h" style="margin-top:12px">Course commencement</div>
    <p>Upon receipt of your enrolment form a Brightfield Training staff member will contact you to conduct a pre-enrolment interview and to confirm your enrolment.</p>
    <div class="h" style="margin-top:12px">Course induction</div>
    <p>All Brightfield Training students will receive a course induction. Inductions may be completed face-to-face, on VoiceLink, or over the phone. During your induction, your trainer will: take time to explain how to navigate your course resources and assessments; and provide you with some guidance on the depth and content expected in some of the different assessments.</p>
  </div>
  <div class="col txt" style="left:190px;top:152px;width:166px">
    <div class="h">First aid</div>
    <p>You have the option of selecting HLTAID003 Provide first aid as an elective unit within this course. Note: selecting this unit is not mandatory. Brightfield Training delivers this unit at select venues around Brisbane. Please contact us to find out upcoming course dates and venues. Alternatively, you are able to complete the first aid course with any provider in Australia. Some important points to consider if selecting HLTAID003 Provide first aid as an elective:</p>
    <ul>
      <li>The cost of the first aid unit is not included in Brightfield Training's course fee. You will need to pay the listed course fee to your selected first aid provider.</li>
      <li>Ensure that you are booking into a first aid course that includes the nationally recognised unit HLTAID003 Provide First Aid.</li>
    </ul>
    <div class="h">Course completion</div>
    <p>On successful completion of all course requirements you will be issued a Nationally Recognised Certificate III in Education Support. All students completing or discontinuing their studies will be required to complete a student survey.</p>
  </div>
  <div class="enrol">
    <div class="notch"></div>
    <div class="how">
      <p style="font-size:6.2px;margin-bottom:4px">HOW TO ENROL</p>
      <p style="margin-bottom:4px">Read the Student Handbook and this Course Outline<br>You have 3 different ways to enrol:</p>
      <p style="margin-bottom:3px"><b>1.</b> Go to brightfieldtraining.com.au/enrol-now to complete your enrolment online OR</p>
      <p style="margin-bottom:3px"><b>2.</b> Download an Enrolment Form from our website and return by email or post OR</p>
      <p><b>3.</b> Call us on 1300 555 214 to enrol over the phone</p>
    </div>
    <div class="brand2">Brightfield Training</div>
    <ul class="contacts">
      <li>BRIGHTFIELD TRAINING RTO # 40817</li>
      <li>PO Box 2214 Kelvin Bay QLD 4172</li>
      <li>1300 555 214</li>
      <li>info@brightfieldtraining.com.au</li>
      <li>www.aidecoursehub.com.au</li>
      <li>www.brightfieldtraining.com.au</li>
    </ul>
  </div>
  <div class="footer-bar"></div>
</section>

</body>
</html>
```